Copper Lantern need a Recruitment ad poster design

We need a poster design to hire a high end sampling team. our target is university students. The message/ad must be witty, challenging, clever, curious, extremely creative and funny.

We need to entice their curiosity about the job and make them apply. The job is offering an attractive salary, learning experience, fun and exposure for students

Target Market(s)

Our target are males and females who are:
Ambitious, Life loving, Great common sense, Smart,Energetic, Social butterfly, Social Intelligence, Individualistic, Dynamic, Committed & Responsible, Passionate, Chameleon, Have great hair, Intelligent
Confident, Beautiful, Charming, Adventurous, Athletic.
Boys should be: "WORK HARD, PLAY HARD", GREAT NET-WORKER
BARNABY QUILLOT :)

Industry/Entity Type

University

Font styles to use
Decorative
Other font styles liked:
• Stylus BT

Requirements
Must have
• Fun and witty message
Should not have
• people wearing suits!
The title "hiring ad"

```html
<!DOCTYPE html>
<html lang="en">
<head>
<meta charset="utf-8">
<title>Copper Lantern Marketing – Hiring Poster</title>
<link rel="stylesheet" href="https://fonts.googleapis.com/css2?family=Tinos:wght@400;700&display=swap">
<style>
  :root {
    --backdrop: #e9e9e7;
    --poster-ink: #161d24;
    --headline: #ffffff;
    --accent: #f4a535;
    --body-text: #ffffff;
    --mascot-red: #c8202f;
    --mascot-teal: #1ba99a;
    --mascot-yellow: #e6df1e;
  }
  * { margin: 0; padding: 0; box-sizing: border-box; }
  html, body {
    width: 1200px; height: 1148px; overflow: hidden;
    background: var(--backdrop);
  }
  .poster {
    position: absolute; left: 230px; top: 24px;
    width: 740px; height: 1100px;
    background: var(--poster-ink);
    overflow: hidden;
    font-family: "Tinos", "Times New Roman", serif;
  }
  .mascot-art {
    position: absolute; left: 440px; top: 165px;
    width: 360px; height: 360px;
  }
  .headline {
    position: absolute; left: 112px; top: 290px;
    color: var(--headline);
    font-weight: 700; font-size: 60px; line-height: 66px;
    letter-spacing: 0.5px;
  }
  .tagline {
    position: absolute; left: 124px; top: 580px;
    color: var(--accent);
    font-weight: 700; font-size: 32px; line-height: 46px;
  }
  .job-details {
    position: absolute; left: 124px; top: 690px;
    color: var(--body-text);
    font-weight: 700; font-size: 26px; line-height: 39px;
  }
  .contact {
    position: absolute; left: 136px; top: 930px;
    display: flex; gap: 14px;
    color: var(--accent);
    font-weight: 700; font-size: 20px; line-height: 26px;
  }
  .contact-divider {
    width: 2px; background: var(--accent); opacity: 0.7;
  }
  .brand-sign {
    position: absolute; right: 46px; bottom: 58px;
    display: flex; align-items: center; gap: 12px;
    color: var(--headline);
    font-weight: 400; font-size: 22px;
  }
  .brand-dot {
    width: 40px; height: 40px; border-radius: 50%;
    background: var(--mascot-teal);
  }
</style>
</head>
<body>
  <main class="poster">
    <svg class="mascot-art" viewBox="0 0 360 360" role="img" aria-label="Colourful round owl mascot illustration with rainbow rings">
      <defs>
        <radialGradient id="mascot-fill" cx="50%" cy="50%" r="50%">
          <stop offset="0%" stop-color="var(--mascot-teal)"/>
          <stop offset="55%" stop-color="var(--mascot-yellow)"/>
          <stop offset="100%" stop-color="var(--mascot-red)"/>
        </radialGradient>
      </defs>
      <circle cx="180" cy="180" r="178" fill="url(#mascot-fill)"/>
    </svg>

    <h1 class="headline">Prvoe<br>taht ure<br>nto a<br>cmpouetr</h1>

    <p class="tagline">If you can read this<br>please apply now.</p>

    <p class="job-details">
      Copper Lantern Marketing is hiring<br>
      university students (girls &amp; boys)<br>
      in the field of sampling.<br>
      If you like to Play hard and work<br>
      hard don't hesitate to contact us
    </p>

    <div class="contact">
      <div class="contact-item">Contact:<br>0790418263</div>
      <span class="contact-divider"></span>
      <div class="contact-item">Email:<br>info@copper-lantern.com</div>
    </div>

    <div class="brand-sign">
      <span class="brand-dot"></span>
      <span class="brand-name">Copper Lantern Marketing</span>
    </div>
  </main>
</body>
</html>
```